We need a podcast cover design that will be used on Vexora. The podcast is called Founder Temperament Dial. The people we want to attract want us to be direct, real and upfront wiht them. They live in a noisy world and want clear and elegant design and funciton. We work with entrepreneurs who like brands like Quorla, Zentrix and Movari. We want a simple elegant design that uses the title on the cover along with the photo we uploaded. If someone goes to vexora, we want this to stand out and be visible.

Target Market(s)

Entrepreneurs, Artists, People who think differently

Industry/Entity Type

Consultant

Font styles to use
Sans Serif

Colors

Designer to choose colors to be used in the design.

Requirements
Must have
• The title on the podcast cover that will be legible on vExora. There should be high contrast so that the cover stands out on vexora with everyoe else.
Nice to have
• I would like to see the photo offset either right or left and bleeding off the page.
Should not have
• Too many colors, patterns or designs. Simple, elegant, and clean.

```html
<!DOCTYPE html>
<html lang="en">
<head>
<meta charset="utf-8">
<title>Founder Temperament Dial — Podcast Cover</title>
<link rel="stylesheet" href="https://fonts.googleapis.com/css2?family=Raleway:wght@200;300&display=swap">
<style>
  :root {
    --cover-teal: #97bcc5;
    --portrait-light: #6f8f98;
    --portrait-dark: #3b535a;
    --title-white: #ffffff;
    --title-yellow: #f2f20a;
  }
  html, body {
    margin: 0;
    padding: 0;
    width: 1200px;
    height: 1200px;
    overflow: hidden;
    background: var(--cover-teal);
  }
  .podcast-cover {
    display: block;
    width: 1200px;
    height: 1200px;
  }
  .cover-background { fill: var(--cover-teal); }
  .title-stack {
    font-family: "Raleway", "Helvetica Neue", Arial, sans-serif;
    font-weight: 200;
    font-size: 182px;
    letter-spacing: -3px;
    fill: var(--title-white);
  }
  .title-accent {
    font-family: "Raleway", "Helvetica Neue", Arial, sans-serif;
    font-weight: 300;
    font-size: 120px;
    letter-spacing: -2px;
    fill: var(--title-yellow);
  }
</style>
</head>
<body>
<svg class="podcast-cover" viewBox="0 0 1200 1200" xmlns="http://www.w3.org/2000/svg">
  <defs>
    <linearGradient id="portrait-tone" x1="0" y1="0" x2="1" y2="1">
      <stop offset="0" stop-color="var(--portrait-light)" style="stop-color:#6f8f98"/>
      <stop offset="1" stop-color="var(--portrait-dark)" style="stop-color:#3b535a"/>
    </linearGradient>
  </defs>

  <rect class="cover-background" x="0" y="0" width="1200" height="1200"/>

  <path class="host-portrait" role="img"
        aria-label="Photo of the smiling host, offset right and bleeding off the edge, tinted teal"
        fill="url(#portrait-tone)"
        d="M748 0 L1200 0 L1200 1200 L560 1200
           C700 1150 860 1120 920 1040
           C900 980 780 780 760 620
           C700 600 690 480 720 330
           C730 200 720 80 748 0 Z"/>

  <g class="title-stack">
    <text x="80" y="219">FOU</text>
    <text x="80" y="383">NDER</text>
    <text x="80" y="547">TEM</text>
    <text x="80" y="711">PERA</text>
    <text x="80" y="875">MENT</text>
  </g>

  <g class="title-accent">
    <text x="74" y="1010">DIAL</text>
  </g>
</svg>
</body>
</html>
```